Insurance Agency website design for Vell Harbor Insurance, LP

Build a website for Vell Harbor Insurance, LP which sells Homeowners, Auto, Renters, Condo, Flood, Disability, Life, Umbrella, and health insurance. We need the coolest insurance agency website out there to get quotes, contact us, or get additional information. Please list the following insurance companies we work with: Dranko, Halvenro, Corvane Mutual, Tremix, Wendmarch, Ostrelby, and Plumeworth.

Make a design similar to https://www.brimlockagents.example/

Selling personal insurance policies

```html
<!DOCTYPE html>
<html lang="en">
<head>
<meta charset="utf-8">
<title>Vell Harbor Insurance, LP</title>
<link href="https://fonts.googleapis.com/css2?family=Montserrat:wght@500;800&family=Poppins:wght@400;500;600&display=swap" rel="stylesheet">
<style>
:root{
  --navy:#122e80;
  --navy-deep:#0d2470;
  --green:#7cc242;
  --green-dark:#4b9a1f;
  --sky:#eaf2fc;
  --ink:#1b1b1b;
  --text:#333;
  --white:#fff;
  --black:#000;
}
*{margin:0;padding:0;box-sizing:border-box}
html,body{width:1200px;height:3275px;overflow:hidden}
body{position:relative;font-family:"Poppins",sans-serif;color:var(--text);background:var(--white)}
.abs{position:absolute}
a{color:inherit;text-decoration:none}

/* top bar */
.topbar{left:651px;top:0;width:549px;height:26px;background:var(--green);clip-path:polygon(0 0,100% 0,100% 100%,24px 100%);color:var(--white);font-size:11px;font-weight:500;display:flex;align-items:center;gap:26px;padding-left:108px}
.topbar span{display:flex;align-items:center;gap:7px}
.topbar .sep{width:1px;height:26px;background:rgba(255,255,255,.5)}

/* header */
.logo{left:105px;top:42px;display:flex;align-items:center;gap:8px}
.logo-mark{width:16px;height:16px;background:var(--green)}
.logo-name{font-family:"Poppins",sans-serif;font-weight:600;font-size:14px;line-height:1.1;color:var(--navy);text-transform:uppercase}
.nav{top:50px;font-size:13px;color:var(--ink);font-weight:500;text-transform:uppercase}
.btn{display:flex;align-items:center;justify-content:center;gap:10px;font-weight:500;border-radius:3px;color:var(--white)}
.btn-quote-top{left:961px;top:38px;width:132px;height:39px;background:var(--navy);font-size:14px}

/* hero */
.hero{left:0;top:98px;width:1200px;height:640px;background:linear-gradient(100deg,#2f56a6 0%,#5479bb 45%,#a6b5cf 75%,#c9c2b4 100%)}
.hero-title{left:140px;top:205px;font-family:"Montserrat",sans-serif;color:var(--white);font-size:45px;line-height:55px}
.hero-title b{font-weight:800}
.hero-title span{font-weight:500}
.hero-text{left:140px;top:386px;width:510px;color:var(--white);font-size:14.5px;line-height:21px}
.btn-hero{left:140px;top:469px;width:205px;height:45px;background:var(--green);font-size:14.5px}
.hero-curve{left:0;top:590px}
.scroll{left:564px;top:691px;width:72px;height:72px;border-radius:50%;background:var(--white);box-shadow:0 4px 14px rgba(0,0,0,.15);display:flex;align-items:center;justify-content:center}

/* about */
.about-photo{left:141px;top:855px;width:424px;height:416px;border-radius:22px;background:linear-gradient(135deg,#9aa0a4,#d7d3cc 55%,#eceae6)}
.about-notch{left:490px;top:855px;width:80px;height:62px;background:var(--white);border-bottom-left-radius:22px}
.stat{left:414px;top:1189px;width:188px;height:133px;background:var(--green-dark);border:7px solid var(--white);border-radius:14px;color:var(--white);text-align:center;padding-top:14px}
.stat strong{display:block;font-size:42px;line-height:46px;font-weight:600}
.stat small{display:block;font-size:17px;line-height:22px}
.tag{left:643px;top:864px;padding:4px 10px;background:#e3efd7;color:#4a6a30;font-size:12px;letter-spacing:1.5px;border-radius:2px}
.about-title{left:643px;top:896px;font-size:28px;font-weight:600;color:var(--ink)}
.about-copy{left:643px;top:950px;width:415px;font-size:14.5px;line-height:21.2px;color:#333}
.about-copy p{margin-bottom:7px}
.btn-read{left:643px;top:1261px;width:134px;height:42px;background:var(--navy);font-size:15px}

/* types */
.types{left:0;top:1404px;width:1200px;height:570px;background:var(--sky)}
.section-title{left:0;width:1200px;text-align:center;font-size:28px;font-weight:600;color:var(--ink)}
.card{top:1549px;width:212px;height:244px;background:var(--navy);border-radius:8px;color:var(--white);text-align:center}
.card.green{background:var(--green-dark)}
.card .icon{margin:26px auto 0;width:96px;height:96px;border-radius:50%;background:rgba(255,255,255,.3);display:flex;align-items:center;justify-content:center}
.card .icon i{width:78px;height:78px;border-radius:50%;background:var(--white);display:flex;align-items:center;justify-content:center}
.card h3{margin-top:16px;font-size:15px;font-weight:600}
.card p{margin:6px auto 0;width:190px;font-size:12px;line-height:17px}
.card .go{position:absolute;left:88px;bottom:-16px;width:36px;height:34px;border-radius:3px;background:var(--green-dark);display:flex;align-items:center;justify-content:center}
.card.green .go{background:var(--navy)}
.card:not(.green) .go{background:#3ea31d}
.btn-all{left:501px;top:1845px;width:197px;height:43px;background:var(--navy);font-size:15px}

/* partners */
.partner{width:161px;height:118px;background:var(--white);border-radius:4px;box-shadow:0 2px 10px rgba(0,0,0,.1);display:flex;align-items:center;justify-content:center;font-size:19px;font-weight:500;color:var(--navy)}

/* quote */
.quote{left:141px;top:2466px;width:917px;height:320px;border-radius:10px;background:linear-gradient(120deg,#1a3592,#213c99 50%,#1c3590);color:var(--white);text-align:center}
.quote h2{margin-top:74px;font-size:28px;font-weight:600}
.quote p{margin:10px auto 0;width:540px;font-size:15px;line-height:21px}
.btn-q{margin:14px auto 0;width:155px;height:42px;background:#44a11f;font-size:15px}

/* footer */
.footer{left:0;top:2871px;width:1200px;height:362px;background:var(--black);color:var(--white)}
.f-title{font-size:20px;font-weight:600}
.f-head{font-size:15.5px;font-weight:500}
.f-head::after{content:"";display:block;width:30px;height:2px;background:var(--white);margin-top:8px}
.f-text{font-size:13.5px;line-height:21px}
.f-list li{list-style:none;font-size:13.5px;margin-bottom:10px;display:flex;align-items:center;gap:8px}
.social li{margin-bottom:13px;gap:6px}
.social b{width:28px;height:28px;border:1px solid var(--white);border-radius:50%;display:inline-block}
.contact div{display:flex;gap:10px;font-size:13.5px;line-height:19px;margin-bottom:14px}
.copy{left:0;top:3233px;width:1200px;height:42px;background:var(--navy-deep);color:var(--white);font-size:12px;display:flex;align-items:center;justify-content:center}
</style>
</head>
<body>

<div class="abs topbar">
  <span><svg width="12" height="12" viewBox="0 0 24 24" fill="#fff"><path d="M6.6 10.8a15.1 15.1 0 006.6 6.6l2.2-2.2a1 1 0 011-.25 11.4 11.4 0 003.6.57 1 1 0 011 1V20a1 1 0 01-1 1A17 17 0 013 4a1 1 0 011-1h3.5a1 1 0 011 1c0 1.25.2 2.45.57 3.6a1 1 0 01-.25 1z"/></svg>Phone: 555-014-2287</span>
  <i class="sep"></i>
  <span><svg width="13" height="10" viewBox="0 0 26 20" fill="#fff"><path d="M0 0h26v20H0z M2 3v1l11 7 11-7V3L13 10z" fill-rule="evenodd"/></svg>E-Mail: info@vellharbor.example</span>
</div>

<div class="abs logo"><i class="logo-mark"></i><span class="logo-name">Vell Harbor<br>Insurance</span></div>
<a class="abs nav" style="left:310px">Home</a>
<a class="abs nav" style="left:391px">About Us</a>
<a class="abs nav" style="left:499px">Insurance <svg width="10" height="7" viewBox="0 0 10 7"><path d="M1 1l4 4 4-4" stroke="#1b1b1b" stroke-width="1.6" fill="none"/></svg></a>
<a class="abs nav" style="left:634px">Market Partners</a>
<a class="abs nav" style="left:803px">Contact</a>
<a class="abs btn btn-quote-top">Get a Quote</a>

<div class="abs hero" role="img" aria-label="Family sitting on the floor of a new home among moving boxes, the father holding a cardboard roof over them"></div>
<h1 class="abs hero-title"><b>Protect What Matters</b><br><span>Most with Trusted</span><br><b>Insurance</b></h1>
<p class="abs hero-text">At Vell Harbor Insurance, we understand how crucial it is to protect the things that matter most to you - your home, health, and family.</p>
<a class="abs btn btn-hero">Get Your Quote Now</a>
<svg class="abs hero-curve" width="1200" height="160" viewBox="0 0 1200 160">
  <polygon points="0,18 600,134 1200,18 1200,160 0,160" fill="var(--green)"/>
  <polygon points="0,50 600,140 1200,32 1200,160 0,160" fill="#fff"/>
</svg>
<div class="abs scroll"><svg width="18" height="30" viewBox="0 0 18 30"><rect x="1.5" y="1.5" width="15" height="27" rx="7.5" stroke="var(--navy)" stroke-width="2" fill="none"/><line x1="9" y1="7" x2="9" y2="12" stroke="var(--navy)" stroke-width="2"/></svg></div>

<div class="abs about-photo" role="img" aria-label="Insurance agent at a laptop advising an older couple at an office table"></div>
<div class="abs about-notch"></div>
<div class="abs stat"><strong>50+</strong><small>Skilled<br>Professionals</small></div>
<span class="abs tag">About Us</span>
<h2 class="abs about-title">VELL HARBOR INSURANCE</h2>
<div class="abs about-copy">
  <p>Vell Harbor Insurance is a full-service, independent insurance agency with over three decades of experience in delivering comprehensive insurance solutions to individuals.</p>
  <p>We proudly offer a diverse portfolio of products from more than 20 of the most reputable and financially secure companies in the industry. Our dedicated team of over 50 skilled professionals is committed to customizing these products and services to meet the unique needs of each client.</p>
  <p>At Vell Harbor Insurance, our experts are focused on addressing the individual needs of our clients, ensuring exceptional service and support at every step.</p>
</div>
<a class="abs btn btn-read">Read More <svg width="10" height="10" viewBox="0 0 10 10"><path d="M2 8l6-6M3 2h5v5" stroke="#fff" stroke-width="1.3" fill="none"/></svg></a>

<section class="abs types"></section>
<h2 class="abs section-title" style="top:1482px">INSURANCE TYPES</h2>

<div class="abs card" style="left:141px">
  <div class="icon"><i><svg width="40" height="40" viewBox="0 0 40 40" fill="none" stroke="var(--navy)" stroke-width="1.8"><path d="M4 20L20 6l16 14M8 17v17h24V17"/><circle cx="20" cy="24" r="6"/><path d="M20 21v6"/></svg></i></div>
  <h3>HOMEOWNERS</h3>
  <p>Lorem Ipsum is simply dummy text of the printing typesetting industry Lorem Ipsum has</p>
  <a class="go"><svg width="10" height="10" viewBox="0 0 10 10"><path d="M2 8l6-6M3 2h5v5" stroke="#fff" stroke-width="1.3" fill="none"/></svg></a>
</div>
<div class="abs card green" style="left:376px">
  <div class="icon"><i><svg width="42" height="40" viewBox="0 0 42 40" fill="none" stroke="var(--navy)" stroke-width="1.8"><path d="M4 26v-6l4-8h16l4 8v6z"/><circle cx="10" cy="27" r="3"/><circle cx="22" cy="27" r="3"/><path d="M30 10l8 3v8c0 5-4 8-8 9"/><path d="M30 18l2 2 4-4"/></svg></i></div>
  <h3>AUTO</h3>
  <p>Lorem Ipsum is simply dummy text of the printing typesetting industry Lorem Ipsum has</p>
  <a class="go"><svg width="10" height="10" viewBox="0 0 10 10"><path d="M2 8l6-6M3 2h5v5" stroke="#fff" stroke-width="1.3" fill="none"/></svg></a>
</div>
<div class="abs card" style="left:611px">
  <div class="icon"><i><svg width="40" height="40" viewBox="0 0 40 40" fill="none" stroke="var(--navy)" stroke-width="1.8"><path d="M11 16L20 8l9 8v9H11z"/><path d="M4 20v8l10 8M36 20v8l-10 8"/><path d="M18 25v-5h4v5"/></svg></i></div>
  <h3>RENTERS</h3>
  <p>Lorem Ipsum is simply dummy text of the printing typesetting industry Lorem Ipsum has</p>
  <a class="go"><svg width="10" height="10" viewBox="0 0 10 10"><path d="M2 8l6-6M3 2h5v5" stroke="#fff" stroke-width="1.3" fill="none"/></svg></a>
</div>
<div class="abs card" style="left:847px">
  <div class="icon"><i><svg width="40" height="40" viewBox="0 0 40 40" fill="none" stroke="var(--navy)" stroke-width="1.8"><circle cx="18" cy="7" r="3"/><path d="M18 12v10h8l4 8"/><circle cx="17" cy="27" r="8"/></svg></i></div>
  <h3>DISABILITY</h3>
  <p>Lorem Ipsum is simply dummy text of the printing typesetting industry Lorem Ipsum has</p>
  <a class="go"><svg width="10" height="10" viewBox="0 0 10 10"><path d="M2 8l6-6M3 2h5v5" stroke="#fff" stroke-width="1.3" fill="none"/></svg></a>
</div>
<a class="abs btn btn-all">View All Insurance <svg width="10" height="10" viewBox="0 0 10 10"><path d="M2 8l6-6M3 2h5v5" stroke="#fff" stroke-width="1.3" fill="none"/></svg></a>

<h2 class="abs section-title" style="top:2052px">OUR PARTNERS</h2>
<div class="abs partner" style="left:244px;top:2116px">Dranko</div>
<div class="abs partner" style="left:427px;top:2116px">Halvenro</div>
<div class="abs partner" style="left:611px;top:2116px">Corvane Mutual</div>
<div class="abs partner" style="left:794px;top:2116px">Wendmarch</div>
<div class="abs partner" style="left:336px;top:2260px">Tremix</div>
<div class="abs partner" style="left:519px;top:2260px">Ostrelby</div>
<div class="abs partner" style="left:702px;top:2260px">Plumeworth</div>

<section class="abs quote">
  <h2>GET A QUOTE TODAY</h2>
  <p>Lorem ipsum dolor sit amet, consectetuer adipiscing elit, sed diam nonummy nibh euismod tincidunt ut laoreet dolore magna aliquam erat volutpat. Ut wisi enim ad minim veniam.</p>
  <a class="btn btn-q">Get a Quote <svg width="10" height="10" viewBox="0 0 10 10"><path d="M2 8l6-6M3 2h5v5" stroke="#fff" stroke-width="1.3" fill="none"/></svg></a>
</section>

<footer class="abs footer">
  <h3 class="abs f-title" style="left:142px;top:89px">VELL HARBOR INSURANCE</h3>
  <p class="abs f-text" style="left:142px;top:144px;width:315px">Lorem ipsum dolor sit amet, consectetuer adipiscing elit, sed diam nonummy nibh euismod tincidunt utted is laoreet dolore magna aliquam erat volutpat. Ut wisi enim ad minim veniam.<br><u>Read More</u></p>

  <h4 class="abs f-head" style="left:512px;top:88px">Quick Links</h4>
  <ul class="abs f-list" style="left:512px;top:141px">
    <li>» Home</li><li>» About Us</li><li>» Insurance Types</li><li>» Contact Us</li><li>» Get a Quote</li>
  </ul>

  <h4 class="abs f-head" style="left:690px;top:88px">Follow Us</h4>
  <ul class="abs f-list social" style="left:690px;top:137px">
    <li><b></b>Friendloop</li><li><b></b>Vidstream</li><li><b></b>Snapgrid</li><li><b></b>Chirper</li>
  </ul>

  <h4 class="abs f-head" style="left:829px;top:88px">Contact Details</h4>
  <div class="abs contact" style="left:829px;top:141px;width:260px">
    <div><svg width="12" height="16" viewBox="0 0 12 16"><path d="M6 0a6 6 0 016 6c0 4-6 10-6 10S0 10 0 6a6 6 0 016-6z" fill="#fff"/><circle cx="6" cy="6" r="2.2" fill="#000"/></svg><span>Address<br>123 Building Name,<br>City Name, State XY-123456.</span></div>
    <div><svg width="13" height="13" viewBox="0 0 24 24" fill="#fff"><path d="M6.6 10.8a15.1 15.1 0 006.6 6.6l2.2-2.2a1 1 0 011-.25 11.4 11.4 0 003.6.57 1 1 0 011 1V20a1 1 0 01-1 1A17 17 0 013 4a1 1 0 011-1h3.5a1 1 0 011 1c0 1.25.2 2.45.57 3.6a1 1 0 01-.25 1z"/></svg><span>Phone<br>(555) 014-3390</span></div>
    <div><svg width="14" height="11" viewBox="0 0 26 20" fill="#fff"><path d="M0 0h26v20H0z M2 3v1l11 7 11-7V3L13 10z" fill-rule="evenodd"/></svg><span>Email<br>info@VellHarborInsurance.example</span></div>
  </div>
</footer>
<div class="abs copy">Copyright © 2025 Vell Harbor Insurance. All Rights Reserved.</div>

</body>
</html>
```